Esthetically Pleasing Core Values and Brand Promise for Accounting Firm

I would like a cohesive design that ties together my core values and brand promise. My firm, Maple Finch Advisory, provides accounting work to small businesses. I prefer modern and clean designs. I want my Core Values and Brand Promise to represent me - sole entrepreneur, married, mother of two kids, modern esthetics, clean lines, organized, colorful (teals, greys, white, yellows)

Industry/Entity Type

Public Accounting

Colors
33b8a4

```html
<!DOCTYPE html>
<html lang="en">
<head>
<meta charset="utf-8">
<title>Maple Finch Advisory – Core Values</title>
<link rel="stylesheet" href="https://fonts.googleapis.com/css2?family=Montserrat:wght@400;500;600;700;800&display=swap">
<style>
  :root {
    --teal: #5aafaf;
    --yellow: #f7ec6e;
    --ink: #4a4a4a;
    --grey: #a0a0a0;
    --paper: #ffffff;
    --backdrop: #ececec;
  }
  html, body {
    margin: 0;
    width: 1200px;
    height: 2554px;
    overflow: hidden;
    background: var(--backdrop);
    font-family: "Montserrat", Arial, sans-serif;
  }
  .flyer {
    position: absolute;
    left: 40px;
    top: 554px;
    width: 800px;
    height: 1032px;
    background: var(--paper);
    transform: scale(1.4);
    transform-origin: 0 0;
    box-shadow: 0 2px 8px rgba(0,0,0,.25);
    overflow: hidden;
    color: var(--ink);
  }
  .abs { position: absolute; }
  .brand-name {
    left: 55px; top: 62px;
    color: var(--teal);
    font-weight: 400;
    line-height: 1;
    letter-spacing: 1px;
  }
  .brand-name .big { display: block; font-size: 46px; margin-bottom: 6px; }
  .brand-name .small { display: block; font-size: 27px; letter-spacing: 2px; }
  .title-core {
    left: 310px; top: 48px;
    font-size: 92px; font-weight: 800;
    letter-spacing: -5px; line-height: 1;
    color: var(--ink);
  }
  .title-band {
    left: 305px; top: 135px;
    width: 495px; height: 88px;
    background: var(--teal);
    border-radius: 4px 0 0 4px;
  }
  .title-values {
    left: 316px; top: 136px;
    font-size: 92px; font-weight: 800;
    letter-spacing: -5px; line-height: 1;
    color: var(--paper);
  }
  .value h3 {
    margin: 0;
    color: var(--teal);
    font-size: 20px; font-weight: 700;
    line-height: 23px;
  }
  .value p {
    margin: 0;
    font-size: 15.5px; font-weight: 600;
    line-height: 19px;
  }
  .value.right { text-align: right; }
  .promise {
    left: 55px; top: 665px;
    width: 691px; height: 84px;
    background: var(--yellow);
    border-radius: 8px;
    text-align: center;
    font-weight: 700;
    font-size: 25px;
    line-height: 26px;
    padding-top: 16px;
    box-sizing: border-box;
    color: #333;
  }
  .service h3 {
    margin: 0 0 6px;
    color: var(--teal);
    font-size: 26px; font-weight: 700;
    letter-spacing: .5px;
  }
  .service p {
    margin: 0;
    font-size: 15.5px; font-weight: 600;
    line-height: 19px;
  }
  .divider {
    left: 367px; top: 785px;
    height: 170px;
    border-left: 1px dotted var(--ink);
  }
  .footer {
    left: 0; top: 988px;
    width: 800px; height: 44px;
    background: var(--teal);
    color: var(--paper);
    text-align: center;
    font-size: 22px;
    line-height: 44px;
    font-weight: 400;
  }
  .footer b { font-weight: 700; }
</style>
</head>
<body>
<main class="flyer">
  <div class="abs brand-name"><span class="big">MAPLE</span><span class="big">FINCH</span><span class="small">ADVISORY</span></div>

  <div class="abs title-core">CORE</div>
  <div class="abs title-band"></div>
  <div class="abs title-values">VALUES</div>

  <section class="abs value" style="left:54px;top:280px;">
    <h3>EMPOWER</h3>
    <p>we are dedicated,<br>appreciative &nbsp;and<br>respectful of people’s<br>time and purpose.</p>
  </section>
  <section class="abs value right" style="right:54px;top:283px;">
    <h3>CLIENT<br>FOCUSED</h3>
    <p>we provide a personal<br>service that goes above the<br>standards of professional care.</p>
  </section>
  <section class="abs value" style="left:52px;top:548px;">
    <h3>RECTITUDE</h3>
    <p>we know the difference between<br>what we have the right to do and<br>what the right thing to do is.</p>
  </section>
  <section class="abs value right" style="right:50px;top:524px;">
    <h3>RELENTLESS</h3>
    <p style="margin-top:6px">we believe that the<br>longer we try to do our best,<br>the better we become.</p>
  </section>

  <!-- connector lines -->
  <svg class="abs" style="left:0;top:0" width="800" height="700" aria-hidden="true">
    <g fill="none" stroke="#4a4a4a" stroke-width="1" stroke-dasharray="1 2">
      <path d="M80 420 V447 H273"/>
      <path d="M80 500 V471 H273"/>
      <path d="M700 420 V447 H505"/>
      <path d="M700 500 V471 H505"/>
    </g>
  </svg>

  <!-- values wheel -->
  <svg class="abs" style="left:280px;top:352px" width="200" height="200" viewBox="0 0 200 200" aria-hidden="true">
    <path d="M100 100 L100 0 A100 100 0 0 1 200 100 Z" fill="var(--yellow)"/>
    <path d="M100 100 L200 100 A100 100 0 0 1 100 200 Z" fill="var(--grey)"/>
    <path d="M100 100 L100 200 A100 100 0 0 1 0 100 Z" fill="var(--ink)"/>
    <path d="M100 100 L0 100 A100 100 0 0 1 100 0 Z" fill="var(--teal)"/>
    <circle cx="100" cy="100" r="68" fill="#fff"/>
    <g font-family="Montserrat, Arial, sans-serif" font-size="18" fill="#fff">
      <text x="24" y="164">04</text>
      <text x="150" y="162">03</text>
      <text x="132" y="30" opacity=".5">02</text>
    </g>
  </svg>

  <!-- icons -->
  <svg class="abs" style="left:255px;top:332px" width="44" height="44" viewBox="0 0 44 44" aria-hidden="true" fill="var(--ink)">
    <circle cx="22" cy="8" r="6"/>
    <path d="M13 26 Q13 16 22 16 Q31 16 31 26 Z"/>
    <path d="M2 18 L8 18 L12 34 L20 38 L20 43 L10 43 L4 34 Z"/>
    <path d="M42 18 L36 18 L32 34 L24 38 L24 43 L34 43 L40 34 Z"/>
  </svg>
  <svg class="abs" style="left:473px;top:326px" width="46" height="46" viewBox="0 0 46 46" aria-hidden="true">
    <circle cx="27" cy="12" r="10" fill="var(--ink)"/>
    <text x="27" y="17.5" text-anchor="middle" font-family="Montserrat, Arial, sans-serif" font-weight="700" font-size="15" fill="#fff">$</text>
    <path d="M2 30 H8 V44 H2 Z M10 31 Q18 26 26 30 H32 Q35 31 32 34 H22 M22 34 H32 L42 28 Q46 28 44 32 L34 40 H10 Z" fill="var(--ink)"/>
  </svg>
  <svg class="abs" style="left:252px;top:508px" width="42" height="34" viewBox="0 0 42 34" aria-hidden="true">
    <rect x="0" y="0" width="42" height="24" fill="var(--ink)"/>
    <g fill="#fff"><rect x="5" y="12" width="3" height="8"/><rect x="10" y="8" width="3" height="12"/><rect x="15" y="4" width="3" height="16"/></g>
    <circle cx="31" cy="12" r="6" fill="none" stroke="#fff" stroke-width="2"/>
    <circle cx="31" cy="12" r="2" fill="#fff"/>
    <path d="M8 24 L12 32 L16 26" stroke="var(--ink)" stroke-width="2" fill="none"/>
  </svg>
  <svg class="abs" style="left:475px;top:506px" width="44" height="36" viewBox="0 0 44 36" aria-hidden="true" fill="var(--ink)">
    <path d="M15 2 H29 V8 H26 V5 H18 V8 H15 Z"/>
    <rect x="0" y="8" width="44" height="11" rx="3"/>
    <rect x="0" y="21" width="44" height="15" rx="3"/>
    <rect x="19" y="16" width="6" height="7" fill="#fff"/>
  </svg>

  <div class="abs promise">BRAND PROMISE<br>TRUST, TRANSPARENCY AND DEPENDABILITY</div>

  <svg class="abs" style="left:55px;top:782px" width="52" height="52" viewBox="0 0 52 52" aria-hidden="true" fill="var(--ink)">
    <path d="M10 0 H30 L40 10 V20 H10 Z"/>
    <rect x="14" y="6" width="12" height="3" fill="#fff"/>
    <rect x="14" y="12" width="16" height="3" fill="#fff"/>
    <rect x="0" y="22" width="52" height="20" rx="2"/>
    <text x="26" y="38" text-anchor="middle" font-family="Montserrat, Arial, sans-serif" font-weight="800" font-size="17" fill="#fff">TAX</text>
    <path d="M10 44 H40 V52 H10 Z"/>
  </svg>
  <section class="abs service" style="left:126px;top:778px;width:215px;">
    <h3>TAX</h3>
    <p>Maple Finch provides all clients with a trusted tax advisor who provides accuracy in all filings and ensures your compliance with all government agencies.</p>
  </section>

  <div class="abs divider"></div>

  <svg class="abs" style="left:386px;top:780px" width="60" height="60" viewBox="0 0 60 60" aria-hidden="true">
    <circle cx="30" cy="30" r="30" fill="var(--ink)"/>
    <circle cx="30" cy="23" r="10" fill="none" stroke="#fff" stroke-width="3"/>
    <path d="M13 48 Q15 36 30 36 Q45 36 47 48" fill="none" stroke="#fff" stroke-width="3"/>
  </svg>
  <section class="abs service" style="left:457px;top:788px;width:300px;">
    <h3>ACCOUNTING</h3>
    <p>Maple Finch provides all clients with<br>a trusted tax advisor who provides<br>accuracy in all filings and ensures<br>your compliance with all<br>government agencies.</p>
  </section>

  <footer class="abs footer">www.<b>maplefinchadvisory</b>.com</footer>
</main>
</body>
</html>
```